Harbour Lantern Fliers and logo design

We need to design a product logo and some informational fliers for a summit quest.
I have attached our Harbour Lantern logo - colours need to be complimentary but not the same, we would like fresh, funky but still professional. We generally communicate in a fairly casual way to reach our market. (We don't like boring)
Clear and simple - not too busy
images are good but not actual photos
Here is our website to give you an idea www.harbourlantern-example.co.nz
The flier is a 3 page document.
The logo is to say Summit Quest. The challenge is based on exercise, connecting with people, giving, learning and taking notice (The 4 keys to brightwater) Once agin the logo needs to be complementary but not the same.
The Harbour lantern logo needs to be on the fliers but the summit quest logo is separate.
Thanks very much!!

```html
<!DOCTYPE html>
<html lang="en">
<head>
<meta charset="utf-8">
<title>Stress Buster – Summit Quest</title>
<link href="https://fonts.googleapis.com/css2?family=Arimo:wght@400;700&display=swap" rel="stylesheet">
<style>
  :root {
    --teal: #086b64;
    --brand-teal: #2aa98f;
    --lime: #9dc55a;
    --lime-box: #a6cb63;
    --orange: #e05a35;
    --ink: #1f1f1f;
    --white: #ffffff;
  }
  * { margin: 0; padding: 0; box-sizing: border-box; }
  html, body { width: 928px; height: 1200px; overflow: hidden; background: var(--white); }
  body { font-family: "Arimo", Arial, sans-serif; color: var(--ink); }
  .flier { position: relative; width: 928px; height: 1200px; overflow: hidden; background: var(--white); }
  .header-shapes { position: absolute; left: 0; top: 0; width: 928px; height: 870px; }

  .quest-logo { position: absolute; left: 34px; top: 42px; display: flex; align-items: center; gap: 10px; }
  .quest-logo .mark { width: 56px; height: 56px; border-radius: 50%; background: var(--brand-teal); }
  .quest-logo .name { font-weight: 700; font-size: 34px; color: var(--brand-teal); letter-spacing: 1px; line-height: 1; }

  .lantern-logo { position: absolute; left: 612px; top: 74px; font-weight: 700; font-size: 34px; line-height: 1.05; color: var(--brand-teal); }

  .hero-figure {
    position: absolute; left: 574px; top: 284px; width: 204px; height: 538px;
    background: linear-gradient(180deg, rgba(255,255,255,0.95), rgba(255,255,255,0.8));
    border-radius: 100px 100px 0 0;
  }
  .title { position: absolute; left: 34px; top: 179px; color: var(--white); font-weight: 700; font-size: 122px; line-height: 100px; letter-spacing: -3px; }
  .tagline { position: absolute; left: 36px; top: 382px; color: var(--white); font-weight: 700; font-size: 27px; line-height: 35px; }
  .intro { position: absolute; left: 36px; top: 546px; width: 496px; color: var(--white); font-size: 14.4px; line-height: 17.6px; }
  .intro p { margin-bottom: 6px; }

  .steps { position: absolute; left: 0; top: 0; width: 928px; height: 1200px; }
  .step-tag {
    position: absolute; left: 48px; width: 174px; height: 42px;
    background: var(--orange); color: var(--white); font-weight: 700; font-size: 24px;
    padding-left: 10px; line-height: 42px;
    clip-path: polygon(0 12%, 88% 12%, 88% 0, 100% 50%, 88% 100%, 88% 88%, 0 88%);
  }
  .step-text { position: absolute; left: 228px; font-size: 15px; line-height: 18px; width: 640px; }

  .observe-box { position: absolute; top: 1016px; height: 69px; background: var(--lime-box); padding: 3px 8px; }
  .observe-box h3 { font-size: 17px; font-weight: 700; line-height: 20px; }
  .observe-box p { font-size: 11.4px; line-height: 14px; }

  .footer-band { position: absolute; left: 0; top: 1100px; width: 928px; height: 100px; background: var(--lime); }
  .footer-panel { position: absolute; left: 35px; top: 1100px; width: 857px; height: 72px; background: var(--white); }
</style>
</head>
<body>
<div class="flier">
  <svg class="header-shapes" viewBox="0 0 928 870" aria-hidden="true">
    <polygon points="0,122 542,122 532,141 0,141" fill="#9dc55a"/>
    <polygon points="0,152 506,152 496,172 928,172 928,822 0,822" fill="#086b64"/>
    <polyline points="602,0 518,166 928,166" fill="none" stroke="#e05a35" stroke-width="5"/>
    <polygon points="344,821 432,821 388,864" fill="#086b64"/>
  </svg>

  <div class="quest-logo"><span class="mark"></span><span class="name">SUMMIT QUEST</span></div>
  <div class="lantern-logo">Harbour<br>lantern</div>

  <div class="hero-figure" role="img" aria-label="White silhouette of a person lifting a barbell"></div>

  <h1 class="title">STRESS<br>BUSTER!</h1>
  <h2 class="tagline">We cannot control<br>what happens to us<br>in life, but we can<br>change the way we react</h2>

  <div class="intro">
    <p>Stress happens because we are allowing fear, anger, disappointment and a host of other negative emotions to navigate our actions. By becoming aware of these emotions and allowing them to simply be, we can begin to gain control of how we react and respond to stressful situations.</p>
    <p>Our experience is always changing. Without awareness, mental patterns related to what we fear and what upsets us make life harder.</p>
    <p>S.T.O.P is a powerful, yet surprisingly basic strategy that helps you to be focused, alert, relaxed and at your emotional best when stressful moments present themselves in your life.</p>
    <p>Simply put, it's a four-step checklist to use anytime you want to ground yourself and get some insight into whatever is going on. The whole idea behind it is that by taking a very brief break—even less than one minute—you can determine the very best action to take in the moment.</p>
  </div>

  <div class="footer-band"></div>
  <div class="footer-panel"></div>

  <div class="steps">
    <div class="step-tag" style="top:864px">S = Stop</div>
    <p class="step-text" style="top:876px">Stop what you are doing: Press the pause button on your thoughts and actions.</p>

    <div class="step-tag" style="top:920px">T = Take</div>
    <p class="step-text" style="top:931px">Take a few deep breaths to centre yourself and bring yourself fully into the present moment.</p>

    <div class="step-tag" style="top:978px">O = Observe</div>
    <p class="step-text" style="top:989px;left:232px">Observe what is going on with your:</p>

    <div class="observe-box" style="left:232px;width:176px"><h3>BODY</h3><p>What physical sensations are you aware of (touch, sight, hearing, taste, smell)?</p></div>
    <div class="observe-box" style="left:413px;width:129px"><h3>EMOTIONS</h3><p>What are you feeling right now?</p></div>
    <div class="observe-box" style="left:547px;width:335px"><h3>MIND</h3><p>What assumptions are your making about your feelings?<br>What is the story you're telling yourself about<br>why you are having them?</p></div>

    <div class="step-tag" style="top:1091px">P = Proceed</div>
    <p class="step-text" style="top:1097px">Proceed with whatever you were doing, making a conscious, intentional choice to incorporate what you just learned.</p>
  </div>
</div>
</body>
</html>
```